verdant terraces simple classy business card design

my name is owen harlow and I run a gardening business aimed at high class verdant terraces. the business name is verdant terraces and our logo was designed on pixel forum .My clientel are anything from residential homes to businesses. I take pride in my work and know that I offer a service like no other in my area.
The business card will be used to represent my business and I want it to be not only rememberable, but simplistic and modern. Eye catching too. Of course I would like it relatable to gardening and appealing to the correct clientel - those being garden enthusiasts, prestigious homes and businesses that are after top of the line gardening services like no other on the market.
I am not a typical lawn mowing business so I don't want a typical card design that represents that. The gardens I work with are generally million dollar properties with owners who are very garden proud looking for upkeep and guidance from me along with sometimes whole new garden designs. I want the business cards to show to my clients that I take pride, as they do, in their garden. And I want them to know from my card that I am a professional, qualified horticulturist offering them a top of the line service for life. I want them to refer my business on. I want them to look at my business card and see class and professionalism in a modern unique bold way.
The card should be simple with the possibility of the logo on the front being embossed/debossed and my details on the back the card should have a organic garden feel it's very important to me that it is absolutely perfect
I am also very open to ideas and suggestions so look forward to seeing the designs. the business logo has been supplied with this project and I want the card to be double sided

Contact info is
Owen Harlow - Managing Director / Horticulturist
Phone : 0481 526 704
Email: owenharlow@verdantterraces.com.au

Target Market(s)

high class gardens residential and commercial

Industry/Entity Type

Gardener

Contact Information for Business Card

Contact info is
Phone : 0481 526 704

PLEASE MAKE CARD DOUBLE SIDED

Requirements
Must have
• organic simple classy modern feel
• must flow with the current logo that has been supplied with this project
• Double sided
• Must explain in a simple way that I deal with high end gardens and I'm a qualified horticulturist
Nice to have
• embossed debossed logo
Should not have
• shouldn't be to busy or cheap looking

```html
<!DOCTYPE html>
<html lang="en">
<head>
<meta charset="UTF-8">
<title>Verdant Terraces – Business Card</title>
<link href="https://fonts.googleapis.com/css2?family=PT+Sans:wght@400&display=swap" rel="stylesheet">
<style>
  :root {
    --backdrop: #eceeec;
    --card-green: #669c59;
    --gold: #cfa544;
    --text-light: #ffffff;
    --photo-sky: #6f8f5c;
    --photo-mid: #9a5a43;
    --photo-ground: #6fae46;
  }
  html, body {
    margin: 0;
    padding: 0;
    width: 1200px;
    height: 854px;
    overflow: hidden;
    background: var(--backdrop);
    font-family: "PT Sans", sans-serif;
  }
  .canvas {
    position: relative;
    width: 1200px;
    height: 854px;
  }
  .card {
    position: absolute;
    top: 173px;
    width: 299px;
    height: 523px;
    background: var(--card-green);
    box-shadow: 0 4px 8px rgba(0,0,0,0.18);
  }
  .card--front { left: 203px; }
  .card--back { left: 606px; }

  .brand {
    position: absolute;
    left: 0;
    top: 74px;
    width: 100%;
    text-align: center;
    color: var(--gold);
    font-weight: 400;
  }
  .brand__mark {
    width: 50px;
    height: 50px;
    border-radius: 50%;
    background: var(--gold);
    margin: 0 auto 10px;
  }
  .brand__name {
    font-size: 27px;
    letter-spacing: 1.5px;
    line-height: 1;
    margin: 0;
  }
  .brand__tagline {
    font-size: 14px;
    letter-spacing: 12px;
    margin: 6px 0 0 12px;
    line-height: 1;
  }

  .rule {
    position: absolute;
    left: 25px;
    width: 248px;
    height: 1.5px;
    background: var(--gold);
  }
  .card--front .rule { top: 271px; }
  .card--back .rule { top: 197px; }

  .contact {
    position: absolute;
    left: 0;
    width: 100%;
    text-align: center;
    color: var(--text-light);
  }
  .contact__name {
    top: 316px;
    font-size: 24px;
    margin: 0;
  }
  .contact__role {
    top: 355px;
    font-size: 14px;
  }
  .contact__details {
    top: 425px;
    font-size: 12.5px;
    line-height: 18px;
  }
  .contact__details p { margin: 0; }

  .garden-view {
    position: absolute;
    left: 0;
    top: 0;
  }
</style>
</head>
<body>
<main class="canvas">
  <section class="card card--front">
    <div class="brand">
      <div class="brand__mark"></div>
      <p class="brand__name">VERDANT</p>
      <p class="brand__tagline">TERRACES</p>
    </div>
    <div class="rule"></div>
    <h1 class="contact contact__name">Owen Harlow</h1>
    <div class="contact contact__role">Managing Director / Horticulturist</div>
    <div class="contact contact__details">
      <p>Phone : 0481 526 704</p>
      <p>Email: owenharlow@verdantterraces.com.au</p>
    </div>
  </section>

  <section class="card card--back">
    <div class="brand">
      <div class="brand__mark"></div>
      <p class="brand__name">VERDANT</p>
      <p class="brand__tagline">TERRACES</p>
    </div>
    <div class="rule"></div>
    <svg class="garden-view" width="299" height="523" viewBox="0 0 299 523">
      <defs>
        <linearGradient id="gardenTones" x1="0" y1="0" x2="0" y2="1">
          <stop offset="0" stop-color="var(--photo-sky)"/>
          <stop offset="0.5" stop-color="var(--photo-mid)"/>
          <stop offset="1" stop-color="var(--photo-ground)"/>
        </linearGradient>
      </defs>
      <polygon role="img" aria-label="Photograph of a formal estate garden with stone steps, shaped shrubs and a manor house"
        points="150,216 272,281 272,433 150,499 28,433 28,281"
        fill="url(#gardenTones)" stroke="var(--gold)" stroke-width="3"/>
    </svg>
  </section>
</main>
</body>
</html>
```